Healthcare/Medical Consultant Company

KTL is a Healthcare Conultant Company. We help doctors manage the business side of their medical practice.
We already have a very basic world press design. We want an upgraded design that conveys partnership, healthcare expertise and healthcare innovation to our client. It needs to have a sleek, clean, modern and inclusive look. Pictures need need to convey diversity (including pictures of people of all races and shows both men and women working together in a healthcare environment to make it better). The Pictures on the home page should particularly illustrate diversity and Healthcare expertise. The company logo is blue and white but the site doesn’t have to follow the exact same theme but the logo needs to blend well with the chosen theme. The logo should ideally be in the header of the website. We would also like the following included in our website:

1. Pages should include: a home page, About Us page, Services page, Get a quote page, Contact Us page, Staff page(where we can add pictures and bio for staff).

2. The Drop down menu for services should have hyperlinks ( for each service)Leading to a page that provides detailed info about that specific service. Our services include: Revenue Cycle Management, Regulatory Compliance, Human Resources Management, & practice Management.

3. Links to social media should in the header or footer of each page.

4. Contact info should be in the footer of each page.

5. Clients should be an email to us from the contact page.

Target Market(s)

Physician Medical Practices

Industry/Entity Type

Medical

Coding

Coded - Design and coding required

Font styles to use
Sans Serif

Colors

Designer to choose colors to be used in the design.

Requirements
Must have
• See project description
Nice to have
• See project description

```html
<!DOCTYPE html>
<html lang="en">
<head>
<meta charset="utf-8">
<title>KTL Health Partners LLC</title>
<link rel="stylesheet" href="https://fonts.googleapis.com/css2?family=Lato:wght@400;700;900&family=Poppins:wght@400;500;600&display=swap">
<style>
:root{
  --blue:#0b56a4;
  --blue-dark:#094a8f;
  --sky:#2a9fd8;
  --ink:#222;
  --text:#555;
  --muted:#8a8a8a;
  --soft:#f5f5f5;
  --white:#fff;
  --line:#e3e3e3;
}
*{box-sizing:border-box;margin:0;padding:0}
html,body{width:1200px;height:2899px;overflow:hidden}
body{font-family:"Lato",sans-serif;color:var(--text);background:var(--white)}
a{color:inherit;text-decoration:none}
.wrap{width:1046px;margin:0 auto;position:relative}

/* header */
.topbar{height:104px}
.topbar .wrap{height:104px;display:flex;align-items:center;justify-content:space-between}
.brand{display:flex;flex-direction:column;align-items:flex-start;padding-top:4px}
.brand-name{font-family:"Poppins",sans-serif;font-weight:600;font-size:44px;line-height:44px;color:var(--blue);letter-spacing:2px;padding-left:52px}
.brand-tag{font-family:"Poppins",sans-serif;font-weight:500;font-size:11.5px;color:var(--ink);letter-spacing:.3px;margin-top:4px}
.contacts{display:flex;gap:70px;margin-right:52px}
.contact{display:flex;align-items:center;gap:14px}
.contact-icon{width:35px;height:35px;background:var(--blue);border-radius:3px;display:flex;align-items:center;justify-content:center}
.contact-label{font-size:15px;color:var(--blue);line-height:20px}
.contact-value{font-size:15px;color:var(--ink);line-height:20px}

.nav{height:52px;background:var(--blue)}
.nav .wrap{height:52px;display:flex;align-items:stretch}
.nav-item{display:flex;align-items:center;padding:0 34px;color:var(--white);font-size:15px}
.nav-item.is-active{background:var(--sky);width:110px;justify-content:center;padding:0}
.nav-quote{margin-left:auto;background:var(--sky);color:var(--white);font-weight:700;font-size:15px;width:126px;display:flex;align-items:center;justify-content:center}

/* hero */
.hero{height:553px;position:relative;overflow:hidden}
.hero-photo{position:absolute;inset:0;background:linear-gradient(90deg,#e9eaeb 0%,#dcdee0 40%,#b9bcc0 62%,#8e949b 78%,#c9ccd0 100%)}
.hero-copy{position:absolute;left:79px;top:196px}
.hero-title{font-family:"Lato",sans-serif;font-weight:900;font-size:26px;color:var(--blue);letter-spacing:.3px}
.hero-sub{font-size:17px;font-weight:700;color:#555;margin-top:20px}
.btn{display:inline-flex;align-items:center;justify-content:center;background:var(--blue);color:var(--white);font-weight:700;font-size:14px;letter-spacing:.4px}
.hero .btn{margin-top:29px;width:135px;height:41px}
.hero-arrow{position:absolute;top:412px;width:38px;height:38px;border-radius:50%;background:var(--blue);display:flex;align-items:center;justify-content:center}
.hero-arrow.prev{left:20px}.hero-arrow.next{right:20px}

/* section headings */
.section-title{text-align:center;font-family:"Poppins",sans-serif;font-weight:500;font-size:26px;color:var(--sky)}
.section-title b{color:var(--blue);font-weight:500}

/* welcome */
.welcome{height:417px;padding-top:58px;text-align:center}
.welcome p{width:620px;margin:0 auto;font-size:15px;line-height:27px;color:var(--text)}
.welcome p.first{margin-top:24px}
.welcome p + p{margin-top:24px}
.welcome .btn{margin-top:38px;width:136px;height:41px}

/* services */
.services{height:594px;background:var(--soft);padding-top:58px}
.service-grid{position:relative;height:470px}
.service{position:absolute;width:320px;text-align:center}
.service-icon{width:84px;height:84px;border-radius:50%;border:2px solid var(--blue);margin:0 auto;display:flex;align-items:center;justify-content:center}
.service-icon span{width:60px;height:60px;border-radius:50%;background:var(--blue);display:flex;align-items:center;justify-content:center}
.service-name{font-size:16.5px;font-weight:700;color:var(--sky);margin-top:20px}
.service-text{font-size:15px;line-height:27px;color:var(--text);margin-top:4px}
.service-text a{color:var(--blue);font-weight:700;text-decoration:underline}

/* team */
.team{height:511px;padding-top:58px}
.team-grid{display:flex;gap:36px;margin-top:34px}
.member{width:234px;height:323px;background:var(--white);box-shadow:0 1px 5px rgba(0,0,0,.18)}
.member-photo{height:240px;position:relative;background:linear-gradient(180deg,#e5e7ea 0%,#c6c9cd 55%,#55595f 80%,#f2f2f2 100%)}
.member-photo.alt{background:linear-gradient(180deg,#eef0f2 0%,#c9cdd1 50%,#2b2b2d 80%,#1c1c1e 100%)}
.member-info{position:absolute;left:0;right:0;bottom:14px;text-align:center}
.member-name{font-family:"Poppins",sans-serif;font-weight:500;font-size:15.5px;color:var(--ink)}
.member-role{font-size:14px;color:var(--muted);margin-top:8px}
.member-photo.alt .member-name{color:var(--white)}
.member-photo.alt .member-role{color:#888}
.social{display:flex;justify-content:center;gap:6px;padding-top:24px}
.social i{width:36px;height:36px;border-radius:50%;border:1.5px solid var(--blue)}
.social i.solid{background:var(--blue)}

/* news */
.news{height:458px;background:var(--soft);padding-top:58px}
.news-grid{display:flex;gap:41px;justify-content:center;margin-top:34px}
.post{width:272px;height:271px;background:var(--white);position:relative}
.post-photo{height:166px;background:linear-gradient(135deg,#c9d6e4 0%,#8ea8c4 55%,#dfe6ee 100%);position:relative}
.post-photo.team-meet{background:linear-gradient(135deg,#eef1f4 0%,#b6bec7 45%,#e5e8ec 100%)}
.post-frame{position:absolute;left:21px;right:21px;top:20px;bottom:-8px;border:2px solid rgba(255,255,255,.9)}
.post-plus{position:absolute;left:50%;top:50%;width:40px;height:40px;margin:-16px 0 0 -20px;border-radius:50%;background:var(--blue);display:flex;align-items:center;justify-content:center}
.post.is-featured .post-plus{background:transparent;border:2px solid var(--white)}
.post-date{font-size:12px;color:var(--muted);padding:16px 0 0 21px}
.post-title{font-family:"Poppins",sans-serif;font-weight:500;font-size:16.5px;line-height:26px;color:#444;padding:12px 21px 0}
.post.is-featured{background:#3a74b6}
.post.is-featured .post-photo{background:linear-gradient(135deg,#3f78b8,#2f67a8)}
.post.is-featured .post-date{color:#d7e3f1}
.post.is-featured .post-title{color:var(--white)}

/* footer */
.footer{height:210px;background:var(--blue);color:var(--white);text-align:center;padding-top:42px}
.footer-links{display:flex;justify-content:center;gap:0;font-size:15px}
.footer-links a{padding:0 22px;position:relative}
.footer-links a + a::before{content:"|";position:absolute;left:-3px}
.footer .social{padding-top:30px;gap:6px}
.footer .social i{border-color:var(--white);background:transparent}
.footer-rule{border:0;border-top:1px solid rgba(255,255,255,.35);margin:20px 77px 0}
.copyright{font-size:15px;font-weight:700;margin-top:20px}
</style>
</head>
<body>

<header class="topbar">
  <div class="wrap">
    <div class="brand">
      <span class="brand-name">KTL</span>
      <span class="brand-tag">KTL Health Partners LLC</span>
    </div>
    <div class="contacts">
      <div class="contact">
        <span class="contact-icon">
          <svg width="18" height="18" viewBox="0 0 24 24"><path fill="#fff" d="M6.6 10.8a15 15 0 0 0 6.6 6.6l2.2-2.2c.3-.3.7-.4 1-.2 1.1.4 2.3.6 3.6.6.6 0 1 .4 1 1V20c0 .6-.4 1-1 1A17 17 0 0 1 3 4c0-.6.4-1 1-1h3.5c.6 0 1 .4 1 1 0 1.3.2 2.5.6 3.6.1.3 0 .7-.2 1z"/></svg>
        </span>
        <div><div class="contact-label">Call Us</div><div class="contact-value">(555) 210-4380</div></div>
      </div>
      <div class="contact">
        <span class="contact-icon">
          <svg width="20" height="16" viewBox="0 0 20 16"><rect x="1" y="1" width="18" height="14" fill="none" stroke="#fff" stroke-width="1.8"/><path d="M1 1l9 7 9-7" fill="none" stroke="#fff" stroke-width="1.8"/></svg>
        </span>
        <div><div class="contact-label">E-mail</div><div class="contact-value">support@ktl.com</div></div>
      </div>
    </div>
  </div>
</header>

<nav class="nav">
  <div class="wrap">
    <a class="nav-item is-active" href="#">Home</a>
    <a class="nav-item" href="#">About Us</a>
    <a class="nav-item" href="#">Services</a>
    <a class="nav-item" href="#">Get A Quote</a>
    <a class="nav-item" href="#">Contact Us</a>
    <a class="nav-quote" href="#">GET A QUOTE</a>
  </div>
</nav>

<section class="hero">
  <div class="hero-photo" role="img" aria-label="Photo of a man and a woman in business attire reviewing a tablet together in a bright office"></div>
  <div class="hero-copy">
    <h1 class="hero-title">KTL HEALTH PARTNERS LLC</h1>
    <p class="hero-sub">Advancing Health Care</p>
    <a class="btn" href="#">CONTACT US</a>
  </div>
  <a class="hero-arrow prev" href="#" aria-label="Previous slide"><svg width="16" height="16" viewBox="0 0 16 16"><path d="M14 8H3M7 3.5 2.5 8 7 12.5" fill="none" stroke="#fff" stroke-width="2"/></svg></a>
  <a class="hero-arrow next" href="#" aria-label="Next slide"><svg width="16" height="16" viewBox="0 0 16 16"><path d="M2 8h11M9 3.5 13.5 8 9 12.5" fill="none" stroke="#fff" stroke-width="2"/></svg></a>
</section>

<section class="welcome">
  <h2 class="section-title">Welcome To <b>KTL Health Partners</b></h2>
  <p class="first">Lorem Ipsum is simply dummy text of the printing and typesetting industry. Lorem Ipsum has been the industry's standard dummy text ever since the 1500s, when an unknown printer took a galley of type and scrambled it to make a type specimen book.</p>
  <p>It has survived not only five centuries, but also the leap into electronic typesetting, remaining essentially unchanged.</p>
  <a class="btn" href="#">LEARN MORE</a>
</section>

<section class="services">
  <h2 class="section-title">Our <b>Services</b></h2>
  <div class="wrap service-grid">
    <div class="service" style="left:1px;top:34px">
      <div class="service-icon"><span><svg width="30" height="30" viewBox="0 0 30 30"><path d="M6 15a9 9 0 0 1 15-6.7M24 15a9 9 0 0 1-15 6.7" fill="none" stroke="#fff" stroke-width="2"/><path d="M21 4v5h-5M9 26v-5h5" fill="none" stroke="#fff" stroke-width="2"/><text x="15" y="19.5" font-family="Lato,sans-serif" font-size="12" font-weight="700" fill="#fff" text-anchor="middle">$</text></svg></span></div>
      <h3 class="service-name">Revenue Cycle Management</h3>
      <p class="service-text">Lorem Ipsum is simply dummy text of the printing and typesetting...<a href="#">Read More</a></p>
    </div>
    <div class="service" style="left:362px;top:34px">
      <div class="service-icon"><span><svg width="28" height="30" viewBox="0 0 28 30"><rect x="5" y="3" width="18" height="24" rx="1.5" fill="none" stroke="#fff" stroke-width="2"/><path d="M9 10h10M9 15h10M9 20h6" stroke="#fff" stroke-width="2"/></svg></span></div>
      <h3 class="service-name">Medical Billing &amp; Coding</h3>
      <p class="service-text">Lorem Ipsum is simply dummy text of the printing and typesetting...<a href="#">Read More</a></p>
    </div>
    <div class="service" style="left:723px;top:34px">
      <div class="service-icon"><span><svg width="30" height="30" viewBox="0 0 30 30"><rect x="5" y="5" width="18" height="20" fill="none" stroke="#fff" stroke-width="2"/><path d="M9 14l3 3 6-7" fill="none" stroke="#fff" stroke-width="2"/><path d="M20 22l6-6" stroke="#fff" stroke-width="2.5"/></svg></span></div>
      <h3 class="service-name">Regulatory Compliance</h3>
      <p class="service-text">Lorem Ipsum is simply dummy text of the printing and typesetting...<a href="#">Read More</a></p>
    </div>
    <div class="service" style="left:182px;top:255px">
      <div class="service-icon"><span><svg width="32" height="28" viewBox="0 0 32 28"><circle cx="16" cy="9" r="4" fill="#fff"/><circle cx="7" cy="12" r="3" fill="#fff"/><circle cx="25" cy="12" r="3" fill="#fff"/><path d="M9 24a7 7 0 0 1 14 0zM2 24a5 5 0 0 1 8-4v4zM30 24a5 5 0 0 0-8-4v4z" fill="#fff"/></svg></span></div>
      <h3 class="service-name">Human Resources Training</h3>
      <p class="service-text">Lorem Ipsum is simply dummy text of the printing and typesetting...<a href="#">Read More</a></p>
    </div>
    <div class="service" style="left:543px;top:255px">
      <div class="service-icon"><span><svg width="30" height="30" viewBox="0 0 30 30"><rect x="4" y="4" width="22" height="14" fill="none" stroke="#fff" stroke-width="2"/><circle cx="9" cy="23" r="2" fill="#fff"/><circle cx="15" cy="23" r="2" fill="#fff"/><circle cx="21" cy="23" r="2" fill="#fff"/><path d="M9 14l4-4 3 3 5-5" fill="none" stroke="#fff" stroke-width="1.8"/></svg></span></div>
      <h3 class="service-name">Staff Education and Training</h3>
      <p class="service-text">Lorem Ipsum is simply dummy text of the printing and typesetting...<a href="#">Read More</a></p>
    </div>
  </div>
</section>

<section class="team">
  <h2 class="section-title">Our <b>Team</b></h2>
  <div class="wrap team-grid">
    <div class="member">
      <div class="member-photo" role="img" aria-label="Portrait of a team member in a grey blazer">
        <div class="member-info"><div class="member-name">Member Name</div><div class="member-role">Position</div></div>
      </div>
      <div class="social"><i class="solid"></i><i></i><i></i></div>
    </div>
    <div class="member">
      <div class="member-photo alt" role="img" aria-label="Portrait of a team member in a dark suit at a desk">
        <div class="member-info"><div class="member-name">Member Name</div><div class="member-role">Position</div></div>
      </div>
      <div class="social"><i class="solid"></i><i></i><i></i></div>
    </div>
    <div class="member">
      <div class="member-photo" role="img" aria-label="Portrait of a team member in a grey blazer">
        <div class="member-info"><div class="member-name">Member Name</div><div class="member-role">Position</div></div>
      </div>
      <div class="social"><i class="solid"></i><i></i><i></i></div>
    </div>
    <div class="member">
      <div class="member-photo" role="img" aria-label="Portrait of a team member in a grey suit and tie">
        <div class="member-info"><div class="member-name">Member Name</div><div class="member-role">Position</div></div>
      </div>
      <div class="social"><i class="solid"></i><i></i><i></i></div>
    </div>
  </div>
</section>

<section class="news">
  <h2 class="section-title">Latest <b>News</b></h2>
  <div class="news-grid">
    <article class="post">
      <div class="post-photo" role="img" aria-label="Photo of two colleagues working together at a laptop">
        <div class="post-frame"></div>
        <span class="post-plus"><svg width="16" height="16" viewBox="0 0 16 16"><path d="M8 2v12M2 8h12" stroke="#fff" stroke-width="2"/></svg></span>
      </div>
      <div class="post-date">27, JULY 2018</div>
      <h3 class="post-title">Lorem Ipsum is simply dummy text of the printing</h3>
    </article>
    <article class="post is-featured">
      <div class="post-photo" role="img" aria-label="Photo of a medical team meeting, tinted blue">
        <div class="post-frame"></div>
        <span class="post-plus"><svg width="16" height="16" viewBox="0 0 16 16"><path d="M8 2v12M2 8h12" stroke="#fff" stroke-width="2"/></svg></span>
      </div>
      <div class="post-date">27, JULY 2018</div>
      <h3 class="post-title">Lorem Ipsum is simply dummy text of the printing</h3>
    </article>
    <article class="post">
      <div class="post-photo team-meet" role="img" aria-label="Photo of doctors and staff talking in a hospital corridor">
        <div class="post-frame"></div>
        <span class="post-plus"><svg width="16" height="16" viewBox="0 0 16 16"><path d="M8 2v12M2 8h12" stroke="#fff" stroke-width="2"/></svg></span>
      </div>
      <div class="post-date">27, JULY 2018</div>
      <h3 class="post-title">Lorem Ipsum is simply dummy text of the printing</h3>
    </article>
  </div>
</section>

<footer class="footer">
  <nav class="footer-links">
    <a href="#">Home</a><a href="#">About Us</a><a href="#">Services</a><a href="#">Get A Quote</a><a href="#">Contact Us</a>
  </nav>
  <div class="social"><i></i><i></i><i></i></div>
  <hr class="footer-rule">
  <p class="copyright">© KTL HEALTH PARTNERS LLC - 2018. All Rights Reserved.</p>
</footer>

</body>
</html>
```